KN Rentals

Need a one page add for insertion in print media that can also be used as email flyer. Attached my rendition, needs improvement. Please incorporate a list of available Tooling/Equipment to include: dirt augers, rock augers, core barrels, drill buckets, clean-out buckets, slurry augers, over-cutters, under-reamers, steel casing, continuous flight augers (CFA), cranes, concrete pumps, crane-mount rigs, augercast set-ups

```html
<!DOCTYPE html>
<html lang="en">
<head>
<meta charset="utf-8">
<title>KN Rentals – Your Drilling Partner</title>
<link href="https://fonts.googleapis.com/css2?family=Oswald:wght@700&family=Roboto:wght@400;700&family=Tinos&display=swap" rel="stylesheet">
<style>
  :root {
    --page-bg: #bcbcbc;
    --blue: #1558ad;
    --blue-deep: #0f4a99;
    --blue-soft: #8db2de;
    --sky: #e8f1fb;
    --yellow: #f4d614;
    --text-dark: #1d2a3a;
    --label-blue: #2f6fb8;
    --white: #ffffff;
  }
  html, body {
    margin: 0;
    width: 1200px;
    height: 862px;
    overflow: hidden;
    background: var(--page-bg);
  }
  .flyer {
    position: absolute;
    left: 285px;
    top: 17px;
    width: 630px;
    height: 828px;
    box-shadow: -8px 8px 14px rgba(0,0,0,0.45);
  }
  .band-blue { fill: var(--blue); }
  .band-deep { fill: var(--blue-deep); }
  .band-soft { fill: var(--blue-soft); }
  .band-yellow { fill: var(--yellow); }
  .photo { stroke: var(--white); stroke-width: 2; }
  .photo-frame { fill: none; stroke: var(--blue); stroke-width: 1.5; }
  .brand-name { font-family: "Roboto", sans-serif; font-weight: 700; font-size: 34px; fill: var(--blue); letter-spacing: 1px; }
  .brand-mark { fill: var(--blue); }
  .tagline { font-family: "Roboto", sans-serif; font-weight: 400; font-size: 15px; fill: var(--blue); }
  .headline { font-family: "Oswald", sans-serif; font-weight: 700; font-size: 54px; fill: var(--white); text-anchor: end; }
  .list-title { font-family: "Tinos", serif; font-size: 16px; fill: var(--label-blue); }
  .equipment-list { font-family: "Tinos", serif; font-size: 13px; fill: var(--text-dark); }
  .contact { font-family: "Tinos", serif; font-size: 10.5px; fill: var(--text-dark); }
  .footer-link { font-family: "Tinos", serif; font-size: 15px; fill: var(--yellow); }
</style>
</head>
<body>
<svg class="flyer" viewBox="0 0 630 828" width="630" height="828" xmlns="http://www.w3.org/2000/svg">
  <defs>
    <linearGradient id="paper" x1="0" y1="0" x2="1" y2="1">
      <stop offset="0" stop-color="#ffffff"/>
      <stop offset="0.6" stop-color="#dce9f7"/>
      <stop offset="1" stop-color="#b9d1ee"/>
    </linearGradient>
    <linearGradient id="rust" x1="0" y1="0" x2="1" y2="1">
      <stop offset="0" stop-color="#8a5a3a"/>
      <stop offset="1" stop-color="#4a3426"/>
    </linearGradient>
    <linearGradient id="yard" x1="0" y1="0" x2="0" y2="1">
      <stop offset="0" stop-color="#7fa6c8"/>
      <stop offset="0.5" stop-color="#7b6a52"/>
      <stop offset="1" stop-color="#5a4a3a"/>
    </linearGradient>
    <linearGradient id="greenyard" x1="0" y1="0" x2="0" y2="1">
      <stop offset="0" stop-color="#5f8a4a"/>
      <stop offset="1" stop-color="#6e5844"/>
    </linearGradient>
    <linearGradient id="pale" x1="0" y1="0" x2="0" y2="1">
      <stop offset="0" stop-color="#c9d6e3"/>
      <stop offset="1" stop-color="#d9d2c6"/>
    </linearGradient>
  </defs>

  <!-- paper -->
  <rect class="paper" width="630" height="828" fill="url(#paper)"/>
  <rect x="60" y="40" width="420" height="760" fill="#c7d8ec" opacity="0.35" role="img" aria-label="Faint drilling rig backdrop"/>

  <!-- structural bands -->
  <rect class="band-yellow" x="296" y="0" width="334" height="32"/>
  <polygon class="band-blue" points="500,32 630,32 630,428 368,428"/>
  <polygon class="band-blue" points="250,550 630,550 630,780 130,780"/>
  <polygon class="band-soft" points="300,428 630,428 630,552 240,552"/>
  <polygon class="band-yellow" points="220,554 630,554 630,658 250,658"/>
  <polygon class="band-deep" points="175,664 630,664 630,776 125,776"/>
  <polygon class="band-blue" points="150,780 630,780 630,828 134,828"/>
  <rect class="band-yellow" x="0" y="806" width="134" height="18"/>

  <!-- brand -->
  <rect class="brand-mark" x="168" y="50" width="44" height="44"/>
  <text class="brand-name" x="224" y="86">KN RENTALS</text>
  <text class="tagline" x="168" y="124">EXPERTS IN THE DRILLING INDUSTRY</text>

  <!-- headline -->
  <text class="headline" x="604" y="176">YOUR</text>
  <text class="headline" x="604" y="242">DRILLING</text>
  <text class="headline" x="604" y="310">PARTNER</text>

  <!-- photo slots -->
  <rect class="photo" x="14" y="130" width="142" height="184" fill="url(#rust)" role="img" aria-label="Rock auger standing upright"/>
  <rect class="photo" x="170" y="226" width="139" height="186" fill="url(#yard)" role="img" aria-label="Stacked steel casing in equipment yard"/>
  <rect class="photo" x="322" y="319" width="139" height="91" fill="url(#yard)" role="img" aria-label="Large casing section on flatbed trailer"/>
  <rect class="photo" x="322" y="439" width="140" height="92" fill="url(#yard)" role="img" aria-label="Augers loaded on trailer"/>
  <rect class="photo" x="475" y="439" width="142" height="92" fill="url(#pale)" role="img" aria-label="Equipment warehouse exterior"/>
  <rect class="photo" x="245" y="562" width="140" height="90" fill="url(#yard)" role="img" aria-label="Under-reamer tool on flatbed"/>
  <rect class="photo" x="398" y="562" width="140" height="90" fill="url(#greenyard)" role="img" aria-label="Drill buckets on trailer"/>
  <rect class="photo" x="168" y="678" width="140" height="92" fill="url(#rust)" role="img" aria-label="Yard of drilling tools"/>
  <rect class="photo" x="322" y="678" width="139" height="92" fill="url(#rust)" role="img" aria-label="Auger flights stacked"/>
  <rect class="photo" x="475" y="678" width="142" height="92" fill="url(#greenyard)" role="img" aria-label="Crane-mount drilling rig"/>

  <!-- equipment list -->
  <text class="list-title" x="16" y="338">Available</text>
  <text class="list-title" x="16" y="358">Tooling/Equipment</text>
  <g class="equipment-list">
    <text x="18" y="392">›</text><text x="30" y="392">Dirt augers</text>
    <text x="18" y="410.6">›</text><text x="30" y="410.6">Rock augers</text>
    <text x="18" y="429.2">›</text><text x="30" y="429.2">Core barrels</text>
    <text x="18" y="447.8">›</text><text x="30" y="447.8">Drill buckets</text>
    <text x="18" y="466.4">›</text><text x="30" y="466.4">Clean-out buckets</text>
    <text x="18" y="485">›</text><text x="30" y="485">Slurry augers</text>
    <text x="18" y="503.6">›</text><text x="30" y="503.6">Over-cutters</text>
    <text x="18" y="522.2">›</text><text x="30" y="522.2">Under-reamers</text>
    <text x="18" y="540.8">›</text><text x="30" y="540.8">Steel casing</text>
    <text x="18" y="559.4">›</text><text x="30" y="559.4">Continuous flight</text>
    <text x="30" y="578">augers (CFA)</text>
    <text x="18" y="596.6">›</text><text x="30" y="596.6">Cranes</text>
    <text x="18" y="615.2">›</text><text x="30" y="615.2">Concrete pumps</text>
    <text x="18" y="633.8">›</text><text x="30" y="633.8">Crane-mount rigs</text>
    <text x="18" y="652.4">›</text><text x="30" y="652.4">Augercast set-ups</text>
  </g>

  <!-- contact -->
  <g class="contact">
    <text x="14" y="700">Ray Dalton</text>
    <text x="14" y="720">Mob. (555) 204-3187</text>
    <text x="14" y="741">4820 Ridge Loop Road,</text>
    <text x="14" y="755">Riverton, Texas</text>
    <text x="14" y="769">78000</text>
  </g>

  <!-- footer -->
  <text class="footer-link" x="156" y="810">rdalton@kndrillrentals.com</text>
  <text class="footer-link" x="614" y="810" text-anchor="end">www.kndrillrentals.com</text>
</svg>
</body>
</html>
```